Irrigation Business needs their business cards modernised and revamped

I would like to keep my current logo, colours and revamp the format of the card.

I would like the card to be clean yet important.

Im not sure if you include texture but i would like the named logo to be indented into the card etc.

show me something alive and free something thats clinical to the point yet has a feel of achievement. i would like people to go nice card.

Target Market(s)

high end clients, corporate, sports field manger, the guys that make the decisions

Industry/Entity Type

Business

Contact Information for Business Card

nformation to be included

Gareth Minchin (Director)
0472958316
gareth@tkwater.biz
www.tomskerrywatering.com

instagram logo
google logo
facebook logo

Colors

Designer to choose colors to be used in the design.

Requirements
Nice to have
• indentations a really nice feel to the card good texture

```html
<!DOCTYPE html>
<html lang="en">
<head>
<meta charset="utf-8">
<title>Tom's Kerry Watering – Business Cards</title>
<link rel="stylesheet" href="https://fonts.googleapis.com/css2?family=Roboto:wght@400;700&display=swap">
<style>
  :root {
    --backdrop: #1f4f9a;
    --brand-blue: #3a65a8;
    --deep-blue: #2d5597;
    --sky-blue: #3fa4dc;
    --light-sky: #8fd0f0;
    --paper: #ffffff;
    --shadow: rgba(8, 24, 56, 0.45);
  }
  * { box-sizing: border-box; margin: 0; padding: 0; }
  html, body {
    width: 1200px;
    height: 1200px;
    overflow: hidden;
  }
  body {
    background: var(--backdrop);
    font-family: "Roboto", Arial, sans-serif;
    position: relative;
  }
  .card {
    position: absolute;
    top: 420px;
    width: 520px;
    height: 312px;
    overflow: hidden;
    box-shadow: 0 18px 30px var(--shadow);
  }
  .card-front { left: 65px; background: var(--brand-blue); }
  .card-back { left: 615px; background: var(--paper); }
  .card-art {
    position: absolute;
    inset: 0;
    width: 520px;
    height: 312px;
  }
  .brand-mark {
    position: absolute;
    left: 50%;
    transform: translateX(-50%);
    border-radius: 50%;
  }
  .card-front .brand-mark {
    top: 52px;
    width: 108px;
    height: 108px;
    background: var(--sky-blue);
  }
  .card-back .brand-mark {
    top: 28px;
    width: 70px;
    height: 70px;
    background: var(--sky-blue);
  }
  .brand-name {
    position: absolute;
    left: 0;
    right: 0;
    text-align: center;
    font-weight: 700;
    letter-spacing: -0.5px;
    white-space: nowrap;
  }
  .card-front .brand-name {
    top: 172px;
    font-size: 33px;
    color: var(--paper);
  }
  .card-back .brand-name {
    top: 108px;
    font-size: 22px;
    color: var(--deep-blue);
  }
  .contact {
    position: absolute;
    top: 180px;
    left: 0;
    right: 0;
    text-align: center;
    color: var(--sky-blue);
  }
  .contact-name {
    font-size: 18px;
    font-weight: 400;
    color: var(--deep-blue);
    margin-bottom: 4px;
  }
  .contact-line {
    font-size: 12px;
    line-height: 15px;
  }
</style>
</head>
<body>

  <section class="card card-front" aria-label="Business card front">
    <svg class="card-art" viewBox="0 0 520 312" aria-hidden="true">
      <path d="M0 276 H300 C322 276 330 262 352 262 H520 V312 H0 Z" fill="var(--sky-blue)"/>
      <path d="M0 288 H300 C316 288 322 284 336 284" fill="none" stroke="var(--brand-blue)" stroke-width="3"/>
      <rect x="0" y="298" width="520" height="14" fill="var(--sky-blue)"/>
    </svg>
    <div class="brand-mark"></div>
    <h1 class="brand-name">TOM'S KERRY WATERING</h1>
  </section>

  <section class="card card-back" aria-label="Business card back">
    <svg class="card-art" viewBox="0 0 520 312" aria-hidden="true">
      <path d="M0 280 H250 C280 280 292 268 322 268 H520" fill="none" stroke="var(--sky-blue)" stroke-width="5"/>
      <path d="M0 290 H260 C292 290 300 276 332 276 H520 V312 H0 Z" fill="var(--brand-blue)"/>
      <circle cx="354" cy="294" r="7" fill="var(--paper)"/>
      <circle cx="416" cy="294" r="7" fill="var(--paper)"/>
      <circle cx="478" cy="294" r="7" fill="var(--paper)"/>
    </svg>
    <div class="brand-mark"></div>
    <h2 class="brand-name">TOM'S KERRY WATERING</h2>
    <div class="contact">
      <p class="contact-name">Gareth Minchin (Director)</p>
      <p class="contact-line">0472958316</p>
      <p class="contact-line">gareth@tkwater.biz</p>
      <p class="contact-line">www.tomskerrywatering.com</p>
    </div>
  </section>

</body>
</html>
```